依頼詳細
値段は入れず、『不安を安心に』『疑問を納得へ』『生活保護のご葬儀 自己負担0円』と言った文言を入れていただきたいです。
葬儀の流れの図も入れていただきたいです。
※添付ファイルを参照ください。
記載項目
電話番号のところは◯にしておいてください
サイズ
A4
ページ数
片面
希望イメージ
シンプル 複雑
単色 カラフル
暗い 明るい
日常 高級
遊び心 厳粛
未来的 伝統的
女性的 男性的
希望する色
赤系
納品ファイル
• 高解像度JPG (.jpg)
• イラストレーター形式 (.ai)
• フォトショップ形式 (.psd)
• PNG形式 (.png)
補足説明
■ 選んだ理由

シンプルで中身がわかりやすく気に入りました

■ 提案者全員のお礼・コメント

ありがとうございます!!また機会がありましたらお願い致します

```html
<!DOCTYPE html>
<html lang="ja">
<head>
<meta charset="utf-8">
<title>生活保護のご葬儀 自己負担0円</title>
<link href="https://fonts.googleapis.com/css2?family=Noto+Sans+JP:wght@400;500;700;900&family=Noto+Serif+JP:wght@700;900&display=swap" rel="stylesheet">
<style>
:root{
  --green:#3f8f3a;
  --green-deep:#2a6b2a;
  --green-pale:#eaf4d8;
  --yellow:#fff3a8;
  --yellow-deep:#f7d94a;
  --blue:#1f5fa8;
  --blue-pale:#e3eef9;
  --red:#d8262c;
  --ink:#222;
  --muted:#555;
  --paper:#fffef6;
}
*{margin:0;padding:0;box-sizing:border-box}
html,body{width:861px;height:1200px;overflow:hidden}
body{font-family:"Noto Sans JP",sans-serif;color:var(--ink);background:var(--paper)}
.flyer{position:relative;width:861px;height:1200px;background:linear-gradient(180deg,#fffbd6 0%,var(--paper) 26%,var(--paper) 100%)}

.headline{position:absolute;top:18px;left:0;width:100%;text-align:center;display:flex;justify-content:center;align-items:flex-end;gap:14px}
.headline .tag{font-family:"Noto Serif JP",serif;font-weight:700;font-size:20px;color:var(--green-deep)}
.headline .main{font-family:"Noto Serif JP",serif;font-weight:900;font-size:42px;color:var(--green-deep);letter-spacing:2px;border-bottom:3px solid var(--yellow-deep);line-height:1.2}
.zero{position:absolute;top:88px;left:0;width:100%;text-align:center;font-family:"Noto Serif JP",serif;font-weight:900;font-size:84px;color:var(--ink);letter-spacing:6px;line-height:1}
.zero .num{color:var(--red);font-size:100px}

.lead{position:absolute;top:212px;left:40px;right:40px;text-align:center}
.lead .catch{font-size:21px;font-weight:700;color:var(--green-deep)}
.lead .catch b{color:var(--red)}
.lead p{margin-top:8px;font-size:13px;line-height:1.6;color:var(--muted)}

.target{position:absolute;top:300px;left:30px;right:30px;height:62px;background:var(--yellow);border:2px solid var(--yellow-deep);border-radius:6px;display:flex;align-items:center;padding:0 14px;gap:12px}
.target .label{background:var(--green);color:#fff;font-weight:700;font-size:15px;padding:6px 10px;border-radius:4px;writing-mode:horizontal-tb}
.target ul{list-style:none;font-size:13px;line-height:1.7;font-weight:500}
.target li::before{content:"■";color:var(--red);margin-right:4px}

.flow{position:absolute;top:378px;left:30px;width:490px}
.flow h2{font-size:17px;color:var(--green-deep);border-left:6px solid var(--green);padding-left:8px;margin-bottom:8px}
.step{position:relative;margin-bottom:13px;padding-left:40px}
.step .no{position:absolute;left:0;top:0;width:30px;height:30px;border-radius:50%;background:var(--blue);color:#fff;font-weight:700;font-size:15px;display:flex;align-items:center;justify-content:center}
.step h3{font-size:16px;color:var(--blue);line-height:30px}
.step p{font-size:11.5px;line-height:1.5;color:var(--muted)}
.step:not(:last-child)::after{content:"";position:absolute;left:10px;bottom:-12px;border:5px solid transparent;border-top:7px solid var(--blue);}
.step.final .no{background:var(--green)}
.step.final h3{color:var(--green-deep)}

.side{position:absolute;top:388px;left:540px;width:295px}
.photo{width:100%;height:120px;border-radius:6px;background:linear-gradient(160deg,#cfe3f3,#9fc2dc 60%,#7aa07a)}
.example{margin-top:14px;border:2px solid var(--blue);border-radius:6px;background:#fff}
.example h4{background:var(--blue);color:#fff;font-size:14px;padding:6px 10px}
.example ul{list-style:none;padding:10px 12px;font-size:12px;line-height:1.8}
.example li{border-bottom:1px dotted #9bb;display:flex;justify-content:space-between}
.example li span:last-child{color:var(--blue);font-weight:700}
.note{margin-top:14px;background:var(--green-pale);border:2px solid var(--green);border-radius:6px;padding:10px 12px;font-size:12px;line-height:1.6;color:var(--green-deep);font-weight:500}
.scene{margin-top:14px;height:110px;border-radius:6px;background:linear-gradient(180deg,#d9ecf7 0%,#bfe0a0 60%,#7fbf5a 100%)}

.footer{position:absolute;left:0;bottom:0;width:100%;height:205px;background:linear-gradient(180deg,#cfe8f5 0%,#a6d486 55%,#5aa13e 100%)}
.contact{position:absolute;left:30px;right:30px;bottom:20px;height:120px;background:rgba(255,255,255,.9);border-radius:8px;display:flex;align-items:center;justify-content:space-between;padding:0 26px}
.contact .ask{font-size:15px;font-weight:700;color:var(--green-deep)}
.contact .tel{display:flex;align-items:center;gap:8px;font-size:38px;font-weight:900;color:var(--red);line-height:1.2}
.contact .hours{font-size:15px;font-weight:700;color:var(--green-deep)}
.org{text-align:right}
.org .name{font-size:22px;font-weight:700;color:var(--ink)}
.org .url{font-size:13px;color:var(--muted)}
</style>
</head>
<body>
<div class="flyer">
  <div class="headline">
    <span class="tag">不安を安心に</span>
    <span class="main">生活保護のご葬儀</span>
    <span class="tag">疑問を納得へ</span>
  </div>
  <div class="zero">自己負担<span class="num">0</span>円</div>

  <div class="lead">
    <div class="catch">ハルカでは<b>生活保護受給者の葬儀（火葬式）</b>を承ります。</div>
    <p>生活保護受給者の方は市区町村福祉事務所・社会福祉課に葬祭扶助の申請をすることにより<br>故人様の尊厳を守り、自己負担なしで御葬儀（火葬式）を執り行うことができます。</p>
  </div>

  <div class="target">
    <span class="label">対象者</span>
    <ul>
      <li>生活保護受給者の方がお亡くなりになった場合</li>
      <li>扶養義務者がいない、または喪主の方が生活保護受給者の場合</li>
    </ul>
  </div>

  <section class="flow">
    <h2>生活保護葬儀の流れ</h2>
    <div class="step"><span class="no">1</span><h3>ご臨終</h3><p>病院や施設でお亡くなりになりましたら、まずは当社へご連絡ください。</p></div>
    <div class="step"><span class="no">2</span><h3>お迎え</h3><p>ご指定の場所まで寝台車でお迎えにあがります。24時間対応いたします。</p></div>
    <div class="step"><span class="no">3</span><h3>ご安置・ご遺体安置</h3><p>ご自宅または当社安置施設にて、故人様を丁寧にお預かりします。</p></div>
    <div class="step"><span class="no">4</span><h3>お打合せ</h3><p>福祉事務所への申請手続きを含め、ご葬儀の内容をご説明いたします。</p></div>
    <div class="step"><span class="no">5</span><h3>ご出棺・火葬</h3><p>ご納棺の後、火葬場へご出棺いたします。最期のお別れをお過ごしください。</p></div>
    <div class="step"><span class="no">6</span><h3>ご収骨</h3><p>火葬後、ご遺骨を骨壷へ納めます。ご遺骨はご家族様へお渡しします。</p></div>
    <div class="step final"><span class="no">7</span><h3>生活保護葬儀のご請求申請</h3><p>葬祭扶助の請求は当社が代行いたしますので、ご負担はございません。</p></div>
  </section>

  <aside class="side">
    <div class="photo" role="img" aria-label="落ち着いた葬儀式場の写真"></div>
    <div class="example">
      <h4>生活保護葬儀例</h4>
      <ul>
        <li><span>寝台車・お迎え</span><span>含む</span></li>
        <li><span>ご安置・ドライアイス</span><span>含む</span></li>
        <li><span>お棺・骨壷一式</span><span>含む</span></li>
        <li><span>火葬料金</span><span>含む</span></li>
        <li><span>申請代行</span><span>含む</span></li>
      </ul>
    </div>
    <div class="note">市役所の生活保護課・福祉事務所の担当者様とも連携して手続きを進めますので、安心してご相談ください。</div>
    <div class="scene" role="img" aria-label="青空と緑の丘の風景イラスト"></div>
  </aside>

  <div class="footer" role="img" aria-label="青空と草原の風景写真">
    <div class="contact">
      <div>
        <div class="ask">まずはご相談・お問い合わせください</div>
        <div class="tel">
          <svg width="34" height="34" viewBox="0 0 24 24" aria-hidden="true"><path fill="#d8262c" d="M6.6 10.8a15.1 15.1 0 0 0 6.6 6.6l2.2-2.2c.3-.3.7-.4 1-.2 1.1.4 2.3.6 3.6.6.6 0 1 .4 1 1V20c0 .6-.4 1-1 1C10.6 21 3 13.4 3 4c0-.6.4-1 1-1h3.5c.6 0 1 .4 1 1 0 1.2.2 2.4.6 3.6.1.3 0 .7-.2 1z"/></svg>
          TEL.000-000-0000
        </div>
        <div class="hours">営業時間9:00〜17:00（年中無休）</div>
      </div>
      <div class="org">
        <div class="name">一般社団法人ハルカ</div>
        <div class="url">https://haruka-sousai.example.jp</div>
      </div>
    </div>
  </div>
</div>
</body>
</html>
```